Business Card Design

New business card design

Target Market(s)

Residential & Commercial Property Managers

Industry/Entity Type

Plumbing Services

Contact Information for Business Card

Name - Owen Tredgold, title - Director, Phone Number - 0431 862 507, email - owen@rvb-plumbing.com.au, Company ABN - 73 215 904 386,

Font styles to use
Sans Serif

Colors
0054AA
0677BA
7BADD7
CADEEF
E8F1F8

```html
<!DOCTYPE html>
<html lang="en">
<head>
<meta charset="utf-8">
<title>RVB Plumbing Services – Business Card</title>
<link href="https://fonts.googleapis.com/css2?family=Montserrat:wght@300;400;500;700&display=swap" rel="stylesheet">
<style>
  :root {
    --stage: #2b2b2b;
    --card: #1a1a1a;
    --accent: #00aeef;
    --muted: #8a7e72;
    --rule: #5a544e;
  }
  * { margin: 0; padding: 0; box-sizing: border-box; }
  html, body { width: 1200px; height: 1200px; overflow: hidden; }
  body {
    background: var(--stage);
    font-family: "Montserrat", sans-serif;
    position: relative;
  }
  .card {
    position: absolute;
    left: 289px;
    width: 622px;
    height: 372px;
    background: var(--card);
    box-shadow: 0 18px 30px rgba(0,0,0,.55);
  }
  .card--front { top: 194px; }
  .card--back { top: 640px; height: 368px; overflow: hidden; }

  .brand { position: absolute; text-align: center; }
  .brand__name {
    color: var(--accent);
    font-weight: 700;
    line-height: 1;
    text-transform: uppercase;
  }
  .brand__tagline {
    color: var(--muted);
    font-weight: 400;
    text-transform: lowercase;
    white-space: nowrap;
  }

  .card--front .brand { left: 0; right: 0; top: 128px; }
  .card--front .brand__name { font-size: 78px; letter-spacing: 10px; padding-left: 10px; }
  .card--front .brand__tagline { margin-top: 36px; font-size: 15px; letter-spacing: 16.5px; padding-left: 16.5px; }

  .card--back .brand { right: 42px; top: 34px; width: 262px; }
  .card--back .brand__name { font-size: 46px; letter-spacing: 6px; padding-left: 6px; }
  .card--back .brand__tagline { margin-top: 24px; font-size: 10px; letter-spacing: 10px; padding-left: 10px; }

  .holder { position: absolute; left: 29px; top: 248px; }
  .holder__name {
    color: var(--accent);
    font-weight: 700;
    font-size: 19px;
    text-transform: uppercase;
    letter-spacing: -.2px;
    line-height: 1.1;
  }
  .holder__title { color: var(--muted); font-size: 15px; font-weight: 400; line-height: 1.35; }

  .divider {
    position: absolute; left: 29px; right: 43px; top: 299px;
    height: 1px; background: var(--rule);
  }
  .contacts { position: absolute; left: 29px; top: 311px; list-style: none; }
  .contacts li {
    display: flex; align-items: center; gap: 6px;
    color: var(--muted); font-size: 14.5px; font-weight: 500; height: 20px;
  }
  .contacts svg { width: 13px; height: 13px; fill: var(--accent); }
  .abn {
    position: absolute; right: 43px; top: 311px;
    color: var(--muted); font-size: 14.5px; font-weight: 500; line-height: 20px;
  }
  .accent-band {
    position: absolute; left: 0; right: 0; bottom: 0; height: 13px;
    background: var(--accent);
  }
</style>
</head>
<body>
  <section class="card card--front">
    <div class="brand">
      <div class="brand__name">RVB</div>
      <div class="brand__tagline">plumbing services</div>
    </div>
  </section>

  <section class="card card--back">
    <div class="brand">
      <div class="brand__name">RVB</div>
      <div class="brand__tagline">plumbing services</div>
    </div>

    <div class="holder">
      <h1 class="holder__name">Owen Tredgold</h1>
      <p class="holder__title">Director</p>
    </div>

    <div class="divider"></div>

    <ul class="contacts">
      <li>
        <svg viewBox="0 0 24 24" aria-hidden="true"><path d="M6.6 10.8a15.1 15.1 0 0 0 6.6 6.6l2.2-2.2a1 1 0 0 1 1-.25 11.4 11.4 0 0 0 3.6.57 1 1 0 0 1 1 1V20a1 1 0 0 1-1 1A17 17 0 0 1 3 4a1 1 0 0 1 1-1h3.5a1 1 0 0 1 1 1c0 1.25.2 2.45.57 3.57a1 1 0 0 1-.25 1z"/></svg>
        0431 862 507
      </li>
      <li>
        <svg viewBox="0 0 24 24" aria-hidden="true"><path d="M3 5h18a1 1 0 0 1 1 1v12a1 1 0 0 1-1 1H3a1 1 0 0 1-1-1V6a1 1 0 0 1 1-1zm1 2.3V17h16V7.3l-8 5.4z"/></svg>
        owen@rvb-plumbing.com.au
      </li>
    </ul>
    <p class="abn">ABN: 73 215 904 386</p>

    <div class="accent-band"></div>
  </section>
</body>
</html>
```